Website Design for a Project Management Consulting Business

I have a logo design already and now I need a website.
I am a project manager and run my own consulting business.
Currently I am under contract with 3 major Kestrelmark 300 companies. I'd like a website I can direct current and future clients.
My job is running IT projects and working with developers to deliver business priorities.
The website should be professional and clean - I work IT projects and would like to incorporate that into any theme.
I'd like the site to have several page or breakoff links - sections would include : about me, about my services, a page to display all of my certification badges, another page to talk about highlights from past projects and so on.
Looking for a collaborative experience.

Industry/Entity Type

Kestrelmark 300 Consulting Firm - Project Management

Coding

Coded - Design and coding required

Number of Pages Required

1 page

Font styles to use
Serif

Colors
0094D4
00A9DD
6FCCEA
C7EBF8
E9F6FB
EE7325
F08F49
F5BC92
FAE3D3
FDF4ED

Requirements
Must have
• Sections that are a must: About Me (bio), About My Services, About my Certifications and Credentials, Experience on Past Projects,
Nice to have
• I have added the logo below - I'd like to use the logo and have it prominent ; should be professional and inviting

```html
<!DOCTYPE html>
<html lang="en">
<head>
<meta charset="utf-8">
<title>Harbor Line Projects LLC</title>
<link href="https://fonts.googleapis.com/css2?family=Roboto:wght@400;500;700&family=Roboto+Condensed:wght@700&display=swap" rel="stylesheet">
<style>
:root{
  --blue:#0a8ad8;
  --blue-dark:#1474c4;
  --navy:#0e3b7a;
  --navy-deep:#0b3470;
  --sky:#e8f5fc;
  --ink:#333;
  --muted:#555;
  --white:#fff;
  --gold:#e0a92a;
  --silver:#b9bcc0;
  --red:#d3262d;
}
*{box-sizing:border-box;margin:0;padding:0}
html,body{width:1200px;height:3448px;overflow:hidden}
body{position:relative;font-family:"Roboto",sans-serif;color:var(--ink);background:var(--white)}
.abs{position:absolute}
a{color:inherit;text-decoration:none}
.cond{font-family:"Roboto Condensed","Roboto",sans-serif;font-weight:700}

/* header */
.topbar{left:0;top:0;width:1200px;height:83px}
.brand{left:98px;top:18px;display:flex;align-items:center;gap:10px}
.brand-mark{width:44px;height:44px;border:3px solid var(--navy)}
.brand-name{color:var(--navy);font-weight:700;font-size:22px;line-height:1.05;letter-spacing:1px}
.brand-name small{display:block;font-size:10px;letter-spacing:4px;font-weight:500}
.contact-top{top:22px;display:flex;align-items:center;gap:10px;font-size:15px;color:var(--navy)}
.icon-ring{width:34px;height:34px;border:1.5px solid var(--navy);border-radius:50%;display:flex;align-items:center;justify-content:center}
.nav{left:0;top:83px;width:1200px;height:51px;background:var(--blue)}
.nav ul{position:absolute;left:98px;top:14px;display:flex;gap:28px;list-style:none;color:var(--white);font-size:16px}
.social{position:absolute;right:98px;top:9px;display:flex;gap:12px}
.social span{width:33px;height:33px;border:1.5px solid var(--white);border-radius:50%}

/* hero */
.hero{left:0;top:134px;width:1200px;height:645px;background:linear-gradient(90deg,#eef2f6 0%,#dfe6ee 40%,#8fa6c2 70%,#5d7699 100%)}
.hero-title{left:105px;top:130px;font-size:52px;line-height:64px;color:var(--blue);font-weight:500}
.hero-title b{font-weight:700}
.hero-title .dark{color:var(--navy)}
.hero-copy{left:109px;top:330px;width:400px;font-size:16px;line-height:26px;color:#222;text-align:justify}
.btn{display:inline-block;background:var(--blue);color:var(--white);font-size:16px;padding:0 24px;height:46px;line-height:46px;box-shadow:3px 3px 0 var(--navy)}
.hero .btn{position:absolute;left:106px;top:426px}

/* about */
.about-frame{left:83px;top:903px;width:410px;height:420px;border:1.5px solid #222}
.about-photo{left:98px;top:918px;width:410px;height:420px;background:linear-gradient(135deg,#c9ccc8,#7d8f9e 55%,#3e5a7a);box-shadow:0 6px 14px rgba(0,0,0,.25)}
.section-title{color:var(--navy);font-size:29px}
.about-text{left:574px;top:996px;width:540px;font-size:14px;line-height:26px;color:var(--muted)}

/* services band */
.band-left{left:0;top:1514px;width:597px;height:449px;background:linear-gradient(160deg,#1a90dc,#0a7ccb)}
.band-right{left:597px;top:1514px;width:603px;height:449px;background:linear-gradient(160deg,#1a4f93,var(--navy-deep))}
.band h3{font-size:29px;line-height:37px;color:var(--white)}
.band p{font-size:16px;line-height:26.5px;color:var(--white)}
.btn-outline{display:inline-block;border:1.5px solid var(--white);color:var(--white);font-size:13px;padding:0 18px;height:37px;line-height:35px}
.diamond{left:540px;top:1680px;width:120px;height:120px;transform:rotate(45deg);background:var(--white);border:4px solid var(--white)}
.diamond i{position:absolute;inset:8px;border:4px solid var(--navy)}

/* certifications */
.cert{width:326px;height:190px;padding:18px 12px}
.cert.active{background:var(--sky);border-radius:4px}
.badge{position:absolute;left:14px;top:12px;width:60px;height:60px;border-radius:50%}
.cert h4{position:absolute;left:92px;top:20px;font-size:16px;color:#222;font-weight:500}
.cert p{position:absolute;left:94px;top:46px;width:214px;font-size:11px;line-height:17px;font-weight:700;color:#333}
.cert .small{position:absolute;left:94px;top:130px;font-size:11px;color:#444}
.cert .learn{position:absolute;left:96px;top:154px;font-size:11px;color:var(--blue);font-weight:700}
.cert .btn{position:absolute;left:190px;top:128px;height:39px;line-height:39px;font-size:14px;padding:0 18px;box-shadow:none}
.dash{width:0;border-left:2px dashed #999}

/* experience */
.exp-shape{left:0;top:2604px}
.exp-photo{top:2642px;height:295px}
.arrow-btn{top:2915px;width:32px;height:33px;background:var(--white);display:flex;align-items:center;justify-content:center}

/* footer */
.footer{left:0;top:2970px;width:1200px;height:478px;background:#1e8fd6;color:var(--white)}
.footer h5{font-size:25px;margin-bottom:24px}
.footer li{list-style:none;font-size:15px;margin-bottom:20px}
.rule{left:112px;top:400px;width:976px;height:1px;background:rgba(255,255,255,.7)}
</style>
</head>
<body>

<header class="abs topbar">
  <div class="abs brand">
    <div class="brand-mark"></div>
    <div class="brand-name"><small>HARBOR LINE</small>PROJECTS LLC</div>
  </div>
  <div class="abs contact-top" style="left:503px">
    <span class="icon-ring"><svg width="16" height="16" viewBox="0 0 24 24"><path d="M6.6 10.8a15 15 0 0 0 6.6 6.6l2.2-2.2c.3-.3.7-.4 1-.2 1.1.4 2.3.6 3.6.6.6 0 1 .4 1 1V20c0 .6-.4 1-1 1A17 17 0 0 1 3 4c0-.6.4-1 1-1h3.5c.6 0 1 .4 1 1 0 1.3.2 2.5.6 3.6.1.3 0 .7-.2 1z" fill="none" stroke="#0e3b7a" stroke-width="1.8"/></svg></span>
    +1 555-014-2290
  </div>
  <div class="abs contact-top" style="left:710px">
    <span class="icon-ring"><svg width="14" height="16" viewBox="0 0 24 28"><path d="M12 2a8 8 0 0 0-8 8c0 6 8 15 8 15s8-9 8-15a8 8 0 0 0-8-8z" fill="none" stroke="#0e3b7a" stroke-width="2.2"/><circle cx="12" cy="10" r="3" fill="#0e3b7a"/></svg></span>
    14760 Sed ut perspiciatis unde omnis iste natus
  </div>
</header>

<nav class="abs nav">
  <ul>
    <li>Home</li><li>About Me</li><li>My Servixes</li><li>My Certifications and Credentials</li><li>Experience on Past Projects</li>
  </ul>
  <div class="social"><span></span><span></span><span></span><span></span></div>
</nav>

<section class="abs hero" role="img" aria-label="Photo of a smiling consultant in a blue suit holding a tablet in a bright office">
  <h1 class="abs hero-title">WELCOME TO<br><b>HARBOR LINE <span class="dark">PROJECTS</span></b><br><b>LLC</b></h1>
  <p class="abs hero-copy">Lorem ipsum dolor sit amet, consectetur adipiscing elit, sed do eiusmod tempor incididunt ut labore et dolore magna aliqua.</p>
  <a class="btn">GET STARTED</a>
</section>

<section class="about">
  <div class="abs about-frame"></div>
  <div class="abs about-photo" role="img" aria-label="Portrait of a smiling project manager wearing glasses and headphones"></div>
  <h2 class="abs section-title cond" style="left:574px;top:928px">ABOUT ME</h2>
  <p class="abs about-text">Lorem ipsum dolor sit amet, consectetur adipiscing elit, sed do eiusmod tempor incididunt ut labore et dolore magna aliqua. Ut enim ad minim veniam, quis nostrud exercitation ullamco laboris nisi ut aliquip ex ea commodo consequat. Duis aute irure dolor in reprehenderit in voluptate velit esse cillum dolore eu fugiat nulla pariatur. Lorem ipsum dolor sit amet, consectetur adipiscing elit, sed do eiusmod tempor incididunt ut labore et dolore magna aliqua. Ut enim ad minim veniam, quis nostrud exercitation ullamco laboris nisi ut aliquip ex ea commodo consequat. sed do eiusmod tempor incididunt ut labore et dolore magna aliqua. Ut enim ad minim veniam, quis nostrud exercitation ullamco laboris nisi ut aliquip ex ea commodo consequat.</p>
  <a class="abs btn" style="left:574px;top:1287px">READ MORE</a>
</section>

<h2 class="abs section-title cond" style="left:0;width:1200px;text-align:center;top:1460px">ABOUT MY SERVICES</h2>
<section class="band">
  <div class="abs band-left" role="img" aria-label="Blue-tinted photo of a team meeting">
    <h3 class="abs cond" style="left:98px;top:48px">PROJECT MANAGEMENT<br>CONSULTING</h3>
    <p class="abs" style="left:98px;top:150px;width:380px">Lorem ipsum dolor sit amet, consectetur adipiscing elit, sed do eiusmod tempor incididunt ut labore et dolore magna aliqua. Lorem ipsum dolor sit amet, consectetur adipiscing elit, sed do eiusmod tempor incididunt ut labore et dolore magna aliqua. Lorem ipsum dolor</p>
    <a class="abs btn-outline" style="left:98px;top:344px">READ MORE</a>
  </div>
  <div class="abs band-right" role="img" aria-label="Navy-tinted photo of a consultant at work">
    <h3 class="abs cond" style="left:126px;top:48px">&nbsp;MY OWN CONSULTING<br>BUSINESS</h3>
    <p class="abs" style="left:126px;top:150px;width:380px">Lorem ipsum dolor sit amet, consectetur adipiscing elit, sed do eiusmod tempor incididunt ut labore et dolore magna aliqua. Lorem ipsum dolor sit amet, consectetur adipiscing elit, sed do eiusmod tempor incididunt ut labore et dolore magna aliqua. Lorem ipsum dolor</p>
    <a class="abs btn-outline" style="left:130px;top:352px">READ MORE</a>
  </div>
  <div class="abs diamond"><i></i></div>
</section>

<h2 class="abs section-title cond" style="left:0;width:1200px;text-align:center;top:2033px">ABOUT MY SERVICES</h2>
<section class="certs">
  <div class="abs dash" style="left:141px;top:2170px;height:160px"></div>
  <div class="abs dash" style="left:484px;top:2170px;height:160px"></div>
  <div class="abs dash" style="left:816px;top:2170px;height:160px"></div>

  <div class="abs cert active" style="left:98px;top:2102px"><span class="badge" style="background:var(--gold)"></span><h4>Certifications and Credentials</h4><p>Lorem ipsum dolor sit amet, consectetur adipiscing elit, sed do eiusmod tempor incididunt ut labore et dolore magna aliqua.</p><span class="small">Magna aliqua.</span><span class="learn">Learn More →</span><a class="btn">READ MORE</a></div>
  <div class="abs cert" style="left:442px;top:2102px"><span class="badge" style="background:var(--silver)"></span><h4>Certifications and Credentials</h4><p>Lorem ipsum dolor sit amet, consectetur adipiscing elit, sed do eiusmod tempor incididunt ut labore et dolore magna aliqua.</p><span class="small">Magna aliqua.</span><span class="learn">Learn More →</span><a class="btn">READ MORE</a></div>
  <div class="abs cert" style="left:780px;top:2102px"><span class="badge" style="background:var(--red)"></span><h4>Certifications and Credentials</h4><p>Lorem ipsum dolor sit amet, consectetur adipiscing elit, sed do eiusmod tempor incididunt ut labore et dolore magna aliqua.</p><span class="small">Magna aliqua.</span><span class="learn">Learn More →</span><a class="btn">READ MORE</a></div>

  <div class="abs cert" style="left:98px;top:2318px"><span class="badge" style="background:var(--gold)"></span><h4>Certifications and Credentials</h4><p>Lorem ipsum dolor sit amet, consectetur adipiscing elit, sed do eiusmod tempor incididunt ut labore et dolore magna aliqua.</p><span class="small">Magna aliqua.</span><span class="learn">Learn More →</span><a class="btn">READ MORE</a></div>
  <div class="abs cert" style="left:442px;top:2318px"><span class="badge" style="background:var(--silver)"></span><h4>Certifications and Credentials</h4><p>Lorem ipsum dolor sit amet, consectetur adipiscing elit, sed do eiusmod tempor incididunt ut labore et dolore magna aliqua.</p><span class="small">Magna aliqua.</span><span class="learn">Learn More →</span><a class="btn">READ MORE</a></div>
  <div class="abs cert" style="left:780px;top:2318px"><span class="badge" style="background:var(--red)"></span><h4>Certifications and Credentials</h4><p>Lorem ipsum dolor sit amet, consectetur adipiscing elit, sed do eiusmod tempor incididunt ut labore et dolore magna aliqua.</p><span class="small">Magna aliqua.</span><span class="learn">Learn More →</span><a class="btn">READ MORE</a></div>
</section>

<section class="experience">
  <svg class="abs exp-shape" width="470" height="366" viewBox="0 0 470 366"><polygon points="0,0 462,0 430,366 0,366" fill="#0e3b7a"/></svg>
  <h2 class="abs cond" style="left:113px;top:2648px;font-size:29px;line-height:39px;color:var(--white)">EXPERIENCE ON<br>PAST PROJECTS</h2>
  <p class="abs" style="left:113px;top:2750px;width:290px;font-size:16px;line-height:26px;color:var(--white)">Sed ut perspiciatis unde omnis iste natus error sit voluptatem dolore mque laudantium, totam rem aperiam, eaque ipsa quae ab illo inventore veritatis et quasi beatae</p>
  <span class="abs arrow-btn" style="left:111px"><svg width="10" height="14" viewBox="0 0 10 14"><path d="M8 1 2 7l6 6" fill="none" stroke="#0a8ad8" stroke-width="2"/></svg></span>
  <span class="abs arrow-btn" style="left:147px"><svg width="10" height="14" viewBox="0 0 10 14"><path d="m2 1 6 6-6 6" fill="none" stroke="#0a8ad8" stroke-width="2"/></svg></span>
  <div class="abs exp-photo" style="left:407px;width:294px;background:linear-gradient(135deg,#2d3c52,#6b7480 55%,#c7a34a)" role="img" aria-label="Team reviewing plans at a desk"></div>
  <div class="abs exp-photo" style="left:710px;width:293px;background:linear-gradient(135deg,#6c6f73,#a88c74 50%,#3c4a5e)" role="img" aria-label="Colleagues looking at a tablet together"></div>
  <div class="abs exp-photo" style="left:1012px;width:188px;background:linear-gradient(135deg,#c9d3dc,#7d90a6)" role="img" aria-label="Business professionals in conversation"></div>
</section>

<footer class="abs footer">
  <div class="abs" style="left:115px;top:100px;display:flex;align-items:center;gap:12px">
    <span style="width:52px;height:52px;border:3px solid var(--white)"></span>
    <span style="font-size:26px;font-weight:700;line-height:1.05;letter-spacing:1px">HARBOR LINE<br>PROJECTS LLC</span>
  </div>
  <p class="abs" style="left:119px;top:205px;width:330px;font-size:17px;line-height:31px">Lorem ipsum dolor sit amet, consectetur adipiscing elit, sed do eiusmod tempor incididunt ut labore et dolore magna aliqua.</p>
  <div class="abs" style="left:543px;top:87px">
    <h5 class="cond">QUICK LINK</h5>
    <ul><li>Home</li><li>About Me</li><li>About My Services</li><li>About my Certifications and Credentials</li><li>Experience on Past Projects</li></ul>
  </div>
  <div class="abs" style="left:848px;top:87px;font-size:15px">
    <h5 class="cond">CONTACT US</h5>
    <div style="display:flex;gap:22px;line-height:31px"><span>⌖</span><span>1471 ipsum dolor sit<br>amet, consectetur<br>adipiscing elit</span></div>
    <div style="display:flex;gap:20px;margin-top:12px"><span>✉</span><span>hello@harborlineprojects.net</span></div>
    <div style="display:flex;gap:22px;margin-top:22px;font-size:18px"><span>✆</span><span>+1 555-014-2290</span></div>
  </div>
  <div class="abs rule"></div>
  <p class="abs" style="left:0;width:1200px;text-align:center;top:430px;font-size:17px">Copyright © 2022 harborlineprojects.net. All Rights Reserved</p>
</footer>

</body>
</html>
```